Vorbel Neutraceuticals Needs a New Label Design!

Vorbel is a neutraceutical line of vitamins, supplements and protein powders. We are looking for a new look/feel for our labels to really make them pop off the shelf.

Some brands we like are:
www.pemsy.com
www.kelvorida.com
www.dubrin.com

We are going to have square bottles and caps that will most likely be white or clear. We'd like a look/feel that uses bold colors and perhaps foil to make the design stand out.

The labels may be different colors for each product, but the general look/feel should be the same. To learn more about Vorbel, take a look at www.qtremedics.com/vorbel.

We are also reformulating to make our products natural, organic and non-GMO. A look gearing more towards a holistic feel might work!

We have a logo that we cannot change, but we are not committed to the colors of it (Orange and green) and it does NOT have to be prominent on the label itself.

Design must utilize our icons (see website and attached files)

Vorbels tagline is: Shaping Strong Lives
Updates

Project Deadline Extended
Reason: We wanted to extend this project to give designers a bit more time to work on it!

Target Market(s)

Women and Men who are serious about their health, women purchasing vitamins for family....

Industry/Entity Type

Health And Wellness

Font styles to use
Decorative

Requirements
Must have
• Must:
• -Utilize our icons
• -Have bold colors
• -Stand out on a shelf
Nice to have
• The "Bel" in "Vorbel" should stand out

```html
<!DOCTYPE html>
<html lang="en">
<head>
<meta charset="utf-8">
<title>Vorbel Krill Oil Label</title>
<link rel="stylesheet" href="https://fonts.googleapis.com/css2?family=Baloo+2:wght@600;800&family=Lato:ital,wght@0,400;0,700;1,400&display=swap">
<style>
  :root{
    --bg:#efeae4;
    --red:#d81e25;
    --red-deep:#a9141a;
    --black:#141414;
    --white:#ffffff;
    --silver-1:#f4f4f4;
    --silver-2:#cfd0d2;
    --text:#2a2a2a;
    --krill:#f3c7b8;
  }
  *{box-sizing:border-box;margin:0;padding:0}
  html,body{width:1200px;height:849px;overflow:hidden;background:var(--bg)}
  body{font-family:"Lato",sans-serif;color:var(--text);position:relative}

  .label{position:absolute;left:50px;top:150px;width:1100px;height:550px;background:var(--white);box-shadow:0 10px 30px rgba(0,0,0,.15);overflow:hidden}
  .label__band-top{position:absolute;left:0;top:0;width:100%;height:26px;background:var(--red)}

  /* back panel */
  .back{position:absolute;left:0;top:26px;width:420px;height:524px;padding:20px 26px 0}
  .back__copy{font-size:11.5px;line-height:1.45;color:#333}
  .back__copy p{margin-bottom:10px}
  .back__copy strong{font-weight:700}
  .back__disclaimer{margin-top:6px;border:1.5px solid var(--black);padding:5px 8px;font-size:10px;font-weight:700;line-height:1.35;text-align:center}
  .back__warning{margin-top:8px;font-size:10.5px;font-weight:700;color:var(--red);text-transform:uppercase;letter-spacing:.2px}
  .back__url{position:absolute;left:0;bottom:34px;width:100%;height:40px;background:var(--black);color:var(--white);font-size:20px;padding:7px 26px}

  /* front panel */
  .front{position:absolute;left:420px;top:26px;width:680px;height:524px;background:linear-gradient(180deg,var(--silver-1) 0%,var(--silver-2) 55%,var(--silver-1) 100%)}
  .front__brand{position:absolute;right:40px;top:28px;display:flex;align-items:center;gap:12px}
  .front__brand-dot{width:18px;height:18px;border-radius:50%;background:var(--red)}
  .front__brand-name{font-family:"Baloo 2",sans-serif;font-weight:600;font-size:64px;line-height:1;color:var(--black)}
  .front__title{position:absolute;left:22px;top:100px;font-family:"Baloo 2",sans-serif;font-weight:800;font-size:118px;line-height:1;color:var(--red);letter-spacing:1px}
  .front__lower{position:absolute;left:0;top:250px;width:100%;height:274px;background:radial-gradient(circle at 30% 55%,var(--red) 0%,var(--red-deep) 100%)}
  .front__banner{position:absolute;left:40px;top:222px;width:440px;height:58px;background:var(--black);border-radius:0 0 10px 10px;color:var(--white);font-size:33px;text-align:center;line-height:58px}
  .front__claim{position:absolute;right:40px;top:292px;color:var(--white);font-style:italic;font-size:21px;line-height:1.35;text-align:right}
  .front__art{position:absolute;left:20px;top:350px;width:190px;height:110px;border-radius:50%;background:radial-gradient(ellipse,var(--krill) 0%,rgba(243,199,184,.2) 70%,transparent 100%)}
  .front__count{position:absolute;left:280px;top:378px;color:var(--white);font-size:20px;line-height:1.3;border-top:1.5px solid var(--white);border-bottom:1.5px solid var(--white);padding:6px 10px}
  .front__badge{position:absolute;left:470px;top:356px;width:74px;height:74px;border-radius:50%;background:var(--white);border:4px solid var(--red-deep);box-shadow:0 0 0 2px var(--white)}
  .icons{position:absolute;left:20px;top:452px;display:flex;gap:14px}
  .icon{width:58px;height:58px;border-radius:50%;background:var(--white);border:2px solid var(--black);display:flex;align-items:center;justify-content:center}
  .icon svg{width:34px;height:34px}
</style>
</head>
<body>
  <div class="label">
    <div class="label__band-top"></div>

    <section class="back">
      <div class="back__copy">
        <p>Lorem ipsum dolor sit amet, consectetur adipiscing elit. Vestibulum quis tortor ut accumsan. Nullam venenatis sed condimentum. Aenean ac metus porta, neque a, ultrices ante. Aenean condimentum nec pharetra. In et tortor nec lacus viverra fermentum. Vestibulum maximus tincidunt. Duis hendrerit ligula vulputate, id mollis turpis elementum. Nullam vulputate in sem vel, rutrum porttitor arcu.</p>
        <p><strong>Nullis neque consequat</strong> mollis dictum. Nam pretium lorem, et faucibus purus malesuada congue dictum vehicula. Pellentesque porttitor nulla id lacus aliquam commodo.</p>
        <p>Lorem ipsum dolor sit amet ornare dictum. Nam tincidunt id auctor nunc rhoncus et. Etiam consequat leo, quis mattis mi pharetra eget. Phasellus urna, sit amet facilisis leo placerat vitae.</p>
      </div>
      <div class="back__disclaimer">These statements have not been evaluated by the Food &amp; Drug Administration. This product is not intended to diagnose, treat, cure or prevent any disease</div>
      <div class="back__warning">Keep out of reach of children, keep in a cool dry place</div>
      <div class="back__url">www.vorbel.com</div>
    </section>

    <section class="front">
      <div class="front__brand">
        <span class="front__brand-dot"></span>
        <span class="front__brand-name">Vorbel</span>
      </div>
      <h1 class="front__title">Krill Oil</h1>
      <div class="front__lower"></div>
      <div class="front__banner">Dietary Supplement</div>
      <p class="front__claim">Excellent source of Omega 3 fatty acids<br>and Vitamins A, E &amp; D</p>
      <div class="front__art" role="img" aria-label="Line illustration of krill"></div>
      <p class="front__count">180 Capsules<br>30 Day Supply</p>
      <div class="front__badge" role="img" aria-label="Non-GMO certification seal"></div>

      <div class="icons">
        <div class="icon" aria-label="Heart health">
          <svg viewBox="0 0 34 34"><path d="M17 29 L5 17 A6.5 6.5 0 0 1 17 9 A6.5 6.5 0 0 1 29 17 Z" fill="var(--black)"/><polyline points="6,18 12,18 14,14 17,22 19,17 28,17" fill="none" stroke="var(--white)" stroke-width="1.8"/></svg>
        </div>
        <div class="icon" role="img" aria-label="Brain health icon">
          <svg viewBox="0 0 34 34"><ellipse cx="17" cy="16" rx="12" ry="10" fill="var(--black)"/></svg>
        </div>
        <div class="icon" role="img" aria-label="Hair health icon">
          <svg viewBox="0 0 34 34"><g stroke="var(--black)" stroke-width="2"><line x1="9" y1="28" x2="11" y2="6"/><line x1="15" y1="28" x2="16" y2="6"/><line x1="21" y1="28" x2="21" y2="6"/><line x1="27" y1="28" x2="26" y2="6"/></g></svg>
        </div>
        <div class="icon" aria-label="Eye health">
          <svg viewBox="0 0 34 34"><path d="M3 17 Q17 4 31 17 Q17 30 3 17 Z" fill="var(--black)"/><circle cx="17" cy="17" r="5" fill="var(--white)"/><circle cx="17" cy="17" r="2.5" fill="var(--black)"/></svg>
        </div>
        <div class="icon" aria-label="Capsules">
          <svg viewBox="0 0 34 34"><rect x="4" y="6" width="20" height="10" rx="5" fill="var(--black)" transform="rotate(-20 14 11)"/><rect x="10" y="18" width="20" height="10" rx="5" fill="var(--black)" transform="rotate(-20 20 23)"/></svg>
        </div>
        <div class="icon" role="img" aria-label="Joint health icon">
          <svg viewBox="0 0 34 34"><rect x="13" y="3" width="8" height="13" rx="3" fill="var(--black)"/><rect x="13" y="19" width="8" height="12" rx="3" fill="var(--black)"/></svg>
        </div>
      </div>
    </section>
  </div>
</body>
</html>
```